Private Practice Dietitian's Business Card

A 2-sided business card for a dietitian (medical nutritionist) in private practice within a natural therapies allied health clinic. The business card needs to imply warmth and professionalism.
Target Market(s)
Doctors who may refer patients to a dietitian and patients themselves who may request dietetic assessment, education and counselling.
Industry/Entity Type
Business
Requirements
Must have
- The business card must be an intense blue on the front at the bottom, gradually lightening towards the top of the card. Please see:
http://example-pinboard.net/remy_hastwell/card-ideas/
for an example from "The quiet of the orchard" book. I'd like an apple tree on the left with a pale silver/grey trunk (like the silver in the book cover)and branches that bends over to the right above the writing. Apples to be a turquoise/aqua colour similar to that in "The quiet of the orchard" book cover. Front cover writing to read:
plateplan
0482 913 276
plateplan@kettlemail.net.au
'plateplan' is one word but I would like the 'my' in turquoise/aqua to match the apples and the 'dietitian' and the phone number and email address in the pale silver/grey to match the tree trunk.
I'd like the plateplan in larger font than the phone number and email address but for all 3 lines of text on the front of the business card to be stretched so they have the same left and right margin. (I hope this makes sense!)
I would like the back of the card to be white and the top section of text to be in the same turquoise/aqua from the apples on the front of the card and to read:
MAREE TOLBIN
Accredited Practising Dietitian (APD)
Bachelor of Health Science (Nutrition & Dietetics) - Honours
Master of Nutrition & Dietetics
This text should be stretched/compacted so that it all has the same left and right margin.
After this text there should be a blank line for spacing before the next section of text, which is to be in the silver/grey of the tree trunk. It should read:
Weight management
Diabetes
Impaired fasting glycaemia
Impaired glucose tolerance
Gestational diabetes
Wellness & general nutrition
Cardiovascular disease
high blood pressure
High cholesterol
High triglycerides
Fatty liver
Constipation
Diverticular disease
Coeliac disease
Irritable bowel syndrome
Gastroesophageal reflux
Lactose intolerance
Gout
Polycystic ovarian syndrome
Fertility
Pregnancy
Breastfeeding
Osteoporosis
Iron deficiency
Vegetarian eating
This set of text can run across the page from left to right and each medical condition could be separated from the next in some way to help with ease of reading. For example perhaps a space, dot and another space could separate the medical conditions. This set of text should be stretched so that the left and right margins of each line is the same. Thank you!
Nice to have
- An easy-to read but 'elegant' font would be nice - but I have no idea which one! Nothing too ornate, but not dull standard Times New Roman/Arial/Comic Sans either!
Should not have
- Times new roman/comic sans/arial fonts

```html
<!DOCTYPE html>
<html lang="en">
<head>
<meta charset="utf-8">
<title>plateplan – business card</title>
<link rel="stylesheet" href="https://fonts.googleapis.com/css2?family=Federo&family=Didact+Gothic&display=swap">
<style>
  :root {
    --stage-light: #d2d2d2;
    --stage-dark: #9b9b9b;
    --card-top: #1f5cb6;
    --card-mid: #123f98;
    --card-bottom: #0a1a64;
    --aqua: #4db8f0;
    --silver: #e8eaf2;
    --trunk: #eef0f5;
    --list-text: #f4f6fb;
  }
  * { margin: 0; padding: 0; box-sizing: border-box; }
  html, body { width: 1200px; height: 900px; overflow: hidden; }
  body {
    position: relative;
    background: radial-gradient(ellipse at 50% 45%, var(--stage-light) 0%, var(--stage-dark) 100%);
    font-family: "Didact Gothic", sans-serif;
  }
  .card {
    position: absolute;
    left: 220px;
    width: 720px;
    overflow: hidden;
    background: linear-gradient(to bottom, var(--card-top) 0%, var(--card-mid) 45%, var(--card-bottom) 100%);
    box-shadow: 0 2px 6px rgba(0,0,0,0.25);
  }
  .card--front { top: 20px; height: 410px; }
  .card--back { top: 464px; height: 416px; }

  .tree-area { position: absolute; top: 0; }
  .card--front .tree-area { left: 0; width: 340px; height: 410px; }
  .card--back .tree-area { right: 0; width: 230px; height: 150px; }

  .brand-block {
    position: absolute;
    left: 190px;
    top: 150px;
    width: 384px;
  }
  .brand-name {
    font-family: "Federo", sans-serif;
    font-size: 86px;
    line-height: 1;
    letter-spacing: 2px;
    color: var(--silver);
    text-align: justify;
    text-align-last: justify;
  }
  .brand-contact {
    margin-top: 18px;
    font-family: "Federo", sans-serif;
    font-size: 22px;
    color: var(--silver);
    display: flex;
    justify-content: space-between;
    align-items: center;
  }
  .brand-contact .sep { font-size: 14px; }

  .credentials {
    position: absolute;
    left: 12px;
    top: 14px;
    width: 340px;
    color: var(--aqua);
    font-family: "Federo", sans-serif;
  }
  .credentials div {
    text-align: justify;
    text-align-last: justify;
    white-space: nowrap;
  }
  .cred-name { font-size: 48px; line-height: 1.05; letter-spacing: 3px; }
  .cred-title { font-size: 21px; line-height: 1.3; }
  .cred-degree { font-size: 12.5px; line-height: 1.4; }
  .cred-master { font-size: 25px; line-height: 1.3; }

  .services {
    position: absolute;
    left: 32px;
    top: 187px;
    width: 660px;
    color: var(--list-text);
    font-size: 16px;
    line-height: 30px;
    letter-spacing: 0.3px;
  }
  .services div {
    text-align: justify;
    text-align-last: justify;
    white-space: nowrap;
  }
</style>
</head>
<body>

<section class="card card--front" aria-label="Card front">
  <svg class="tree-area" viewBox="0 0 340 410" role="img" aria-label="Illustration of a pale silver apple tree with aqua apples, trunk on the left edge bending over the top">
    <defs>
      <linearGradient id="treeCrown" x1="0" y1="0" x2="1" y2="1">
        <stop offset="0" stop-color="#eef0f5" stop-opacity="0.9"/>
        <stop offset="1" stop-color="#4db8f0" stop-opacity="0.25"/>
      </linearGradient>
    </defs>
    <rect x="0" y="0" width="40" height="410" fill="var(--trunk)"/>
    <path d="M0 0 H330 Q300 150 140 130 Q60 130 40 210 V0 Z" fill="url(#treeCrown)"/>
  </svg>

  <div class="brand-block">
    <div class="brand-name">plateplan</div>
    <div class="brand-contact">
      <span>0482 913 276</span>
      <span class="sep">•</span>
      <span>plateplan@kettlemail.net.au</span>
    </div>
  </div>
</section>

<section class="card card--back" aria-label="Card back">
  <svg class="tree-area" viewBox="0 0 230 150" role="img" aria-label="Illustration of pale silver apple tree branches with aqua apples in the top right corner">
    <defs>
      <linearGradient id="branchCrown" x1="1" y1="0" x2="0" y2="1">
        <stop offset="0" stop-color="#eef0f5" stop-opacity="0.9"/>
        <stop offset="1" stop-color="#4db8f0" stop-opacity="0.2"/>
      </linearGradient>
    </defs>
    <path d="M20 0 H230 V150 Q200 70 110 80 Q40 80 20 0 Z" fill="url(#branchCrown)"/>
  </svg>

  <div class="credentials">
    <div class="cred-name">MAREE TOLBIN</div>
    <div class="cred-title">Accredited Practising Dietitian (APD)</div>
    <div class="cred-degree">Bachelor of Health Science (Nutrition &amp; Dietetics) - Honours</div>
    <div class="cred-master">Master of Nutrition &amp; Dietetics</div>
  </div>

  <div class="services">
    <div>Weight management • Diabetes • Impaired fasting glycaemia • Impaired</div>
    <div>glucose tolerance • Gestational diabetes • Wellness &amp; general nutrition •</div>
    <div>Cardiovascular disease • High blood pressure • High cholesterol • High</div>
    <div>triglycerides • Fatty liver • Constipation • Diverticular disease • Coeliac</div>
    <div>disease • Irritable bowel syndrome • Gastroesophageal reflux • Lactose</div>
    <div>intolerance • Gout • Polycystic ovarian syndrome • Fertility • Pregnancy •</div>
    <div>Breastfeeding • Osteoporosis • Iron deficiency • Vegetarian eating</div>
  </div>
</section>

</body>
</html>
```